Leadership training for women Business + Spirit

I need a flyer for a leadership training to hand out after I've been doing public speaking. I would also like to send it as a PDF. so maybe A4 is a good size. I will probably also need a brochure, with some more in depth information, but to start with I like to just give them something so they get inspired to contact me for more information. You can see more of my style on www.brightlantern.se . Its a training that combines business with spirit, heart with intellect. We focus both on strict leadership skills such as Setting objectives aligned with strategy, assess performance and spiritual practices such as meditation, connecting with your unique essence. I like the deign to communicate business and professional together with warmth, life and joy. Colourful with style. Empowerment. The attached style guide does not have to be followed strictly but please use it in combination with my site www.brightlantern.se I've the logo in many different sizes. I've added the smallest one below. Use any images that you think might fit, doesn't have to be from my website, it could be from your resources. I've added some other images here in the brief too, I have many more but can't attach all of it :-).
Women in leadership positions age 30 - 60
Leadership

```html
<!DOCTYPE html>
<html lang="sv">
<head>
<meta charset="utf-8">
<title>Bright Lantern – Leadership Training for Women</title>
<link href="https://fonts.googleapis.com/css2?family=Libre+Baskerville:wght@400;700&family=Mulish:wght@400;600;800&display=swap" rel="stylesheet">
<style>
  :root {
    --backdrop: #f1d6d2;
    --navy: #1c3553;
    --beige: #c9b8a2;
    --beige-light: #e6dccf;
    --paper: #ffffff;
    --paper-warm: #fbf8f3;
    --ink: #2b2b2b;
    --leaf-green: #5f7a3c;
    --leaf-pink: #c2436a;
    --skin: #b98a6a;
  }
  * { box-sizing: border-box; margin: 0; padding: 0; }
  html, body { width: 1200px; height: 900px; overflow: hidden; }
  body {
    background: var(--backdrop);
    font-family: "Mulish", sans-serif;
    color: var(--ink);
    position: relative;
  }
  .spread {
    position: absolute;
    left: 220px;
    top: 182px;
    width: 760px;
    height: 537px;
    display: flex;
    box-shadow: 0 12px 30px rgba(90, 50, 50, 0.18);
  }
  .panel { position: relative; width: 380px; height: 537px; overflow: hidden; }

  /* ---------- back panel ---------- */
  .panel--back { background: var(--paper-warm); }
  .hero-photo {
    position: absolute; left: 0; top: 0; width: 380px; height: 150px;
    background:
      radial-gradient(ellipse 70px 60px at 215px 70px, rgba(194, 67, 106, 0.9), rgba(194, 67, 106, 0) 70%),
      radial-gradient(ellipse 160px 120px at 80px 60px, #9fb66a, rgba(159, 182, 106, 0) 80%),
      linear-gradient(120deg, #6f8c45, var(--leaf-green) 55%, #3f5a2a);
  }
  .hero-wave { position: absolute; left: 0; top: 96px; width: 380px; height: 70px; }
  .back-content { position: absolute; left: 0; top: 160px; width: 380px; padding: 0 22px; }
  .brand-title {
    font-family: "Libre Baskerville", serif;
    font-weight: 700;
    color: var(--navy);
    font-size: 19px;
    letter-spacing: 0.5px;
    text-align: center;
    margin-bottom: 7px;
  }
  .intro {
    font-size: 6.6px; line-height: 1.5; text-align: center; color: #3a3a3a;
  }
  .pillars { display: flex; gap: 10px; margin-top: 13px; }
  .pillar { flex: 1; text-align: center; }
  .pillar__image {
    width: 54px; height: 54px; margin: 0 auto 6px; border-radius: 50%;
    border: 3px solid var(--beige); box-shadow: 0 0 0 2px var(--paper-warm), 0 0 0 3px var(--beige-light);
  }
  .pillar__image--portrait { background: radial-gradient(circle at 50% 45%, #f1c7c3, #d98a93 70%, #b8727a); }
  .pillar__image--field { background: radial-gradient(circle at 50% 40%, #f4e3c4, #c9a6c6 65%, #9c7fa5); }
  .pillar__image--raised { background: radial-gradient(circle at 50% 45%, #f0d2b4, #c9936b 65%, #8f5f44); }
  .pillar__title {
    font-weight: 800; font-size: 6.8px; color: var(--navy); letter-spacing: 0.3px; margin-bottom: 3px;
  }
  .pillar__text { font-size: 6.2px; line-height: 1.45; text-align: justify; text-align-last: center; color: #3a3a3a; }
  .pillar__quote { font-size: 6.4px; line-height: 1.4; font-weight: 800; margin-top: 5px; color: var(--ink); }

  .footer {
    position: absolute; left: 0; bottom: 0; width: 380px; height: 68px;
    display: flex; align-items: center; justify-content: space-between; padding: 0 20px;
  }
  .footer--navy { background: var(--navy); color: var(--paper); }
  .footer--white { background: var(--paper); color: var(--navy); }
  .contact { font-family: "Libre Baskerville", serif; font-weight: 700; font-size: 10.5px; line-height: 1.75; }
  .contact__row { display: flex; align-items: center; gap: 6px; }
  .contact__icon { width: 9px; height: 9px; flex: none; }
  .wordmark { display: flex; align-items: center; gap: 7px; }
  .wordmark__dot { width: 30px; height: 30px; border-radius: 50%; border: 1.5px solid currentColor; }
  .wordmark__name { font-family: "Libre Baskerville", serif; font-weight: 400; font-size: 17px; }

  /* ---------- front panel ---------- */
  .panel--front { background: var(--paper); }
  .cover-photo {
    position: absolute; left: 0; top: 0; width: 380px; height: 469px;
    background:
      radial-gradient(ellipse 180px 140px at 340px 40px, rgba(255, 246, 222, 1), rgba(255, 246, 222, 0) 75%),
      radial-gradient(ellipse 120px 160px at 250px 260px, rgba(185, 138, 106, 0.95), rgba(185, 138, 106, 0) 75%),
      radial-gradient(ellipse 200px 150px at 200px 420px, #6f6a66, rgba(111, 106, 102, 0) 80%),
      linear-gradient(160deg, #f4ead6 0%, #d9c3a6 35%, #9a8472 70%, #6b5f58 100%);
  }
  .cover-title { position: absolute; left: 24px; top: 40px; display: flex; gap: 4px; color: var(--navy); }
  .cover-title__bar { width: 4px; background: var(--navy); }
  .cover-title__small { font-family: "Libre Baskerville", serif; font-size: 13px; letter-spacing: 0.5px; line-height: 1; }
  .cover-title__large { font-family: "Libre Baskerville", serif; font-weight: 700; font-size: 36px; line-height: 1; letter-spacing: 0.5px; }
</style>
</head>
<body>
  <main class="spread">
    <!-- back panel -->
    <section class="panel panel--back">
      <div class="hero-photo" role="img" aria-label="Photo of a plant with pink leaves against a soft green background"></div>
      <svg class="hero-wave" viewBox="0 0 380 70" preserveAspectRatio="none" aria-hidden="true">
        <path d="M0 40 C90 10 170 70 260 40 C310 24 350 20 380 24 L380 70 L0 70 Z" fill="#c9b8a2"/>
        <path d="M0 48 C90 18 170 78 260 48 C310 32 350 28 380 32" fill="none" stroke="#1c3553" stroke-width="3"/>
        <path d="M0 54 C90 24 170 84 260 54 C310 38 350 34 380 38 L380 70 L0 70 Z" fill="#fbf8f3"/>
      </svg>
      <div class="back-content">
        <h2 class="brand-title">BRIGHT LANTERN</h2>
        <p class="intro">Vi har blivit duktiga på att prestera men tappat kontakten med kropp och själ. Ett holistiskt ledarskap handlar om människor som leder med både hjärta och intellekt, som vågar vara sårbara och växer i sina relationer. Världen behöver ledare som står stadigt i sig själva. Det feminina kan leda oss dit.</p>
        <div class="pillars">
          <article class="pillar">
            <div class="pillar__image pillar__image--portrait" role="img" aria-label="Portrait photo of a smiling woman"></div>
            <h3 class="pillar__title">LEDARSKAP</h3>
            <p class="pillar__text">Som modern ledare möter du många krav. Här tränar du de grundläggande verktygen: att sätta mål i linje med strategin, följa upp resultat och coacha ditt team med närvaro. Du lär dig leda med både huvud och hjärta, och att skapa balans mellan prestation och välmående.</p>
            <p class="pillar__quote">"Att leda är att lyckas genom andra."</p>
          </article>
          <article class="pillar">
            <div class="pillar__image pillar__image--field" role="img" aria-label="Photo of a flower field in soft evening light"></div>
            <h3 class="pillar__title">VARANDET</h3>
            <p class="pillar__text">Genom meditation och stillhet får du kontakt med din unika essens. Vi utforskar vad det innebär att vara, inte bara göra. När du vilar i dig själv blir dina beslut klarare och ditt ledarskap mer äkta. Här finns plats för både tystnad och glädje.</p>
            <p class="pillar__quote">"We are not humans having a spiritual experience. We are spirit having a human experience."</p>
          </article>
          <article class="pillar">
            <div class="pillar__image pillar__image--raised" role="img" aria-label="Photo of a raised fist against a warm sky"></div>
            <h3 class="pillar__title">EMPOWERMENT</h3>
            <p class="pillar__text">Vi lever i en kultur som länge har hållit tillbaka kvinnors röster. Bright Lantern är en samlingsplats som stärker dig, både som människa och ledare, så att du kan kliva fram och ta din plats med trygghet och värme. Det är empowerment.</p>
            <p class="pillar__quote">"Women are the greatest untapped natural resource on this planet."</p>
          </article>
        </div>
      </div>
      <footer class="footer footer--navy">
        <div class="contact">
          <div class="contact__row">
            <svg class="contact__icon" viewBox="0 0 24 24" aria-hidden="true"><path fill="currentColor" d="M6.6 10.8a15.1 15.1 0 0 0 6.6 6.6l2.2-2.2a1 1 0 0 1 1-.25 11.4 11.4 0 0 0 3.6.57 1 1 0 0 1 1 1V20a1 1 0 0 1-1 1A17 17 0 0 1 3 4a1 1 0 0 1 1-1h3.5a1 1 0 0 1 1 1c0 1.25.2 2.45.57 3.57a1 1 0 0 1-.25 1z"/></svg>
            <span>0700-55 18 26</span>
          </div>
          <div class="contact__row">
            <svg class="contact__icon" viewBox="0 0 24 24" aria-hidden="true"><path fill="currentColor" d="M2 5h20v14H2z"/><path fill="none" stroke="#1c3553" stroke-width="2" d="M2 6l10 7 10-7"/></svg>
            <span>hello(a)brightlantern.se</span>
          </div>
        </div>
        <div class="wordmark">
          <span class="wordmark__dot"></span>
          <span class="wordmark__name">Bright Lantern</span>
        </div>
      </footer>
    </section>

    <!-- front panel -->
    <section class="panel panel--front">
      <div class="cover-photo" role="img" aria-label="Photo of a woman's hand in a meditation gesture, wearing gold rings, in warm soft light"></div>
      <h1 class="cover-title">
        <span class="cover-title__bar"></span>
        <span>
          <span class="cover-title__small">LEADERSHIP TRAINING</span><br>
          <span class="cover-title__large">FOR WOMEN</span>
        </span>
      </h1>
      <footer class="footer footer--white">
        <div class="contact">
          <div class="contact__row">
            <svg class="contact__icon" viewBox="0 0 24 24" aria-hidden="true"><path fill="currentColor" d="M6.6 10.8a15.1 15.1 0 0 0 6.6 6.6l2.2-2.2a1 1 0 0 1 1-.25 11.4 11.4 0 0 0 3.6.57 1 1 0 0 1 1 1V20a1 1 0 0 1-1 1A17 17 0 0 1 3 4a1 1 0 0 1 1-1h3.5a1 1 0 0 1 1 1c0 1.25.2 2.45.57 3.57a1 1 0 0 1-.25 1z"/></svg>
            <span>0700-55 18 26</span>
          </div>
          <div class="contact__row">
            <svg class="contact__icon" viewBox="0 0 24 24" aria-hidden="true"><path fill="currentColor" d="M2 5h20v14H2z"/><path fill="none" stroke="#ffffff" stroke-width="2" d="M2 6l10 7 10-7"/></svg>
            <span>hello(a)brightlantern.se</span>
          </div>
        </div>
        <div class="wordmark">
          <span class="wordmark__dot"></span>
          <span class="wordmark__name">Bright Lantern</span>
        </div>
      </footer>
    </section>
  </main>
</body>
</html>
```